The company Velquist needs a design for CBD capsules

We (Velquist) need a new design for our CBD capsules. We already have a design for CBD oil. However, we do not want to use this completely. The Talmbex label and the cans serve as a template. Please upload in the format 139mm x 59mm incl.
2mm bleed all around and in .pdf vector. The logo files for Velquist are included in the briefing.

Industry/Entity Type

Onlineshop

Colors
00AB8E
00BBA5
67D7C9
C6EFE9
E9F9F6

Requirements
Must have
• Please in the format 139mm x 59mm incl. 2mm bleed all around and .pdf vector
Should not have
• It shouldn't be the same label, but it should be recognizable.

```html
<!DOCTYPE html>
<html lang="en">
<head>
<meta charset="utf-8">
<title>Velquist CBD Capsules Label</title>
<link href="https://fonts.googleapis.com/css2?family=Playfair+Display:wght@800;900&family=Source+Serif+4:wght@700&family=Allura&display=swap" rel="stylesheet">
<style>
  :root {
    --backdrop: #dfe8e5;
    --mint-pale: #e9f9f6;
    --mint-soft: #c6efe9;
    --mint-mid: #67d7c9;
    --teal-bright: #00bba5;
    --teal-brand: #00ab8e;
    --teal-dark: #007a66;
    --ink: #1f2a28;
    --silver: #f4f7f7;
  }
  * { box-sizing: border-box; margin: 0; padding: 0; }
  html, body {
    width: 1200px; height: 1200px; overflow: hidden;
    background: var(--backdrop);
  }
  .label {
    position: absolute; left: 30px; top: 358px;
    width: 1140px; height: 484px; overflow: hidden;
    background: linear-gradient(90deg, var(--mint-soft) 0%, var(--mint-pale) 50%, var(--mint-soft) 100%);
  }
  .label-art { position: absolute; inset: 0; width: 1140px; height: 484px; }
  .brand {
    position: absolute; top: 36px; left: 0; width: 100%;
    display: flex; justify-content: center; align-items: center; gap: 12px;
    font-family: "Playfair Display", Georgia, serif; font-weight: 800;
    font-size: 50px; line-height: 1; color: var(--teal-dark);
  }
  .brand-dot {
    width: 12px; height: 12px; border-radius: 50%; background: var(--teal-brand);
  }
  .product-name {
    position: absolute; left: 420px; top: 100px;
    font-family: "Playfair Display", Georgia, serif; font-weight: 900;
    font-size: 130px; line-height: 1; color: var(--ink); letter-spacing: -1px;
  }
  .product-form {
    position: absolute; left: 428px; top: 236px;
    font-family: "Source Serif 4", Georgia, serif; font-weight: 700;
    font-size: 34px; line-height: 1; color: var(--ink); letter-spacing: 1px;
  }
  .claims {
    position: absolute; left: 330px; top: 287px; list-style: none;
    font-family: "Source Serif 4", Georgia, serif; font-weight: 700;
    font-size: 21px; line-height: 28px; color: var(--ink);
  }
  .strength {
    position: absolute; left: 340px; top: 410px; width: 110px; height: 74px;
    border-radius: 10px 10px 0 0; background: var(--mint-soft);
    font-family: "Source Serif 4", Georgia, serif; font-weight: 700;
    font-size: 36px; line-height: 1; color: var(--ink);
    display: flex; justify-content: center; padding-top: 18px;
  }
  .spectrum {
    position: absolute; left: 650px; top: 392px;
    font-family: "Allura", cursive; font-size: 50px; line-height: 1;
    color: #ffffff;
  }
</style>
</head>
<body>
  <div class="label">
    <svg class="label-art" viewBox="0 0 1140 484" xmlns="http://www.w3.org/2000/svg">
      <defs>
        <linearGradient id="teal-band" x1="0" y1="0" x2="1" y2="0">
          <stop offset="0" stop-color="#67d7c9"/>
          <stop offset="0.3" stop-color="#00ab8e"/>
          <stop offset="0.55" stop-color="#00bba5"/>
          <stop offset="1" stop-color="#008f78"/>
        </linearGradient>
      </defs>
      <rect x="0" y="12" width="1140" height="8" fill="url(#teal-band)"/>
      <g role="img" aria-label="Faint hemp leaf pattern in the background">
        <ellipse cx="1040" cy="110" rx="70" ry="80" fill="#67d7c9" opacity="0.18"/>
        <ellipse cx="120" cy="150" rx="75" ry="85" fill="#67d7c9" opacity="0.18"/>
        <ellipse cx="190" cy="320" rx="60" ry="60" fill="#67d7c9" opacity="0.14"/>
        <ellipse cx="960" cy="270" rx="65" ry="55" fill="#67d7c9" opacity="0.14"/>
      </g>
      <ellipse role="img" aria-label="Fan of white leaves beside the product name" cx="810" cy="185" rx="105" ry="110" fill="#ffffff" opacity="0.6"/>
      <path d="M0,400 C400,390 750,352 1140,336 L1140,484 L0,484 Z" fill="url(#teal-band)"/>
      <path d="M0,393 C400,383 750,345 1140,329" fill="none" stroke="var(--silver)" stroke-width="7"/>
    </svg>

    <div class="brand"><span class="brand-dot"></span>Velquist</div>
    <div class="product-name">CBD</div>
    <div class="product-form">CAPSULES</div>
    <ul class="claims">
      <li>- VEGAN</li>
      <li>- GENTECHNIK FREI</li>
    </ul>
    <div class="strength">20%</div>
    <div class="spectrum">Full Spektrum</div>
  </div>
</body>
</html>
```